Stationery and business cards - New design

I need following designs
- writing paper for business letters A4, you can take the data from our old paper. There should just be a place for a third bank account.
- writing paper for business letters (only design + logo, without address, bank accounts and legal data)
- business cards with qr code, one side, only German language (you can take the data from the old layout)

Target Market(s)

Industrial customers

Industry/Entity Type

sheet metal technology, laser cutting of metal sheet

Requirements
Must have
• The address above the recipient should be placed like on my old paper. No relationship to the old design (only color) - please make a completely new design.
Nice to have
• colors like in my new logo
Should not have
• - the business letter should be suitable for borderless print - the green timber in my old paper is very bad for this - so please make a design without a timber (or a timber like it is on my old paper)

```html
<!DOCTYPE html>
<html lang="de">
<head>
<meta charset="utf-8">
<title>Geschäftsausstattung – Falkenried Metallbau</title>
<link rel="stylesheet" href="https://fonts.googleapis.com/css2?family=Montserrat:wght@700&family=Lato:wght@400&display=swap">
<style>
  :root {
    --navy: #1b3a8a;
    --teal: #12808f;
    --grey-text: #8a8a8a;
    --paper: #ffffff;
    --backdrop: #e9eaec;
  }
  * { box-sizing: border-box; margin: 0; padding: 0; }
  html, body { width: 1155px; height: 1200px; overflow: hidden; }
  body { background: var(--backdrop); position: relative; font-family: "Lato", sans-serif; }

  .sheet, .card { position: absolute; background: var(--paper); overflow: hidden; }

  .letterhead { left: 40px; top: 101px; width: 706px; height: 998px; }
  .card-front { left: 775px; top: 283px; width: 343px; height: 213px; }
  .card-back  { left: 772px; top: 530px; width: 350px; height: 213px; }

  .brand { position: absolute; display: flex; align-items: center; gap: 8px; }
  .brand-dot { border-radius: 50%; background: var(--teal); flex: none; }
  .brand-name {
    font-family: "Montserrat", sans-serif; font-weight: 700; color: var(--navy);
    line-height: 1.05; letter-spacing: 0.02em;
  }
  .letterhead .brand { left: 22px; top: 22px; }
  .letterhead .brand-dot { width: 52px; height: 52px; }
  .letterhead .brand-name { font-size: 22px; }

  .card-front .brand { left: 73px; top: 83px; }
  .card-front .brand-dot { width: 46px; height: 46px; }
  .card-front .brand-name { font-size: 19px; }

  .card-back .brand { left: 23px; top: 23px; gap: 6px; }
  .card-back .brand-dot { width: 32px; height: 32px; }
  .card-back .brand-name { font-size: 14px; }

  .band { position: absolute; left: 0; display: block; }
  .letterhead .band { top: 958px; width: 706px; height: 16px; }
  .card-front .band { top: 184px; width: 343px; height: 12px; }
  .card-back .band { top: 187px; width: 350px; height: 12px; }

  .holder { position: absolute; right: 26px; top: 22px; text-align: right; }
  .holder-name { font-family: "Montserrat", sans-serif; font-weight: 700; font-size: 10.5px; color: var(--navy); letter-spacing: 0.02em; }
  .holder-role { font-size: 7.5px; color: var(--grey-text); line-height: 1.3; }
  .holder-rule { width: 26px; height: 1px; background: var(--teal); margin: 4px 0 0 auto; }

  .contacts { position: absolute; left: 23px; top: 94px; list-style: none; }
  .contacts li { display: flex; align-items: flex-start; gap: 5px; font-size: 7.5px; color: var(--grey-text); line-height: 1.3; margin-bottom: 6px; }
  .contacts li.address { margin-bottom: 12px; }
  .contact-icon { width: 10px; height: 10px; flex: none; }
</style>
</head>
<body>

<section class="sheet letterhead" aria-label="Briefbogen">
  <div class="brand">
    <span class="brand-dot"></span>
    <span class="brand-name">FALKENRIED<br>METALLBAU</span>
  </div>
  <svg class="band" viewBox="0 0 706 16" aria-hidden="true">
    <polygon points="0,4 326,4 338,14 0,14" fill="var(--teal)"/>
    <line x1="330" y1="9.5" x2="706" y2="9.5" stroke="var(--navy)" stroke-width="1"/>
  </svg>
</section>

<section class="card card-front" aria-label="Visitenkarte Vorderseite">
  <div class="brand">
    <span class="brand-dot"></span>
    <span class="brand-name">FALKENRIED<br>METALLBAU</span>
  </div>
  <svg class="band" viewBox="0 0 343 12" aria-hidden="true">
    <line x1="0" y1="6.5" x2="180" y2="6.5" stroke="var(--navy)" stroke-width="1"/>
    <polygon points="178,11 186,2 343,2 343,11" fill="var(--teal)"/>
  </svg>
</section>

<section class="card card-back" aria-label="Visitenkarte Rückseite">
  <div class="brand">
    <span class="brand-dot"></span>
    <span class="brand-name">FALKENRIED<br>METALLBAU</span>
  </div>

  <div class="holder">
    <p class="holder-name">MARTA KELLER</p>
    <p class="holder-role">Dipl.-Wirtschaftsing. (FH)</p>
    <p class="holder-role">Geschäftsführerin</p>
    <div class="holder-rule"></div>
  </div>

  <ul class="contacts">
    <li class="address">
      <svg class="contact-icon" viewBox="0 0 10 10" aria-hidden="true"><rect width="10" height="10" rx="1.5" fill="var(--navy)"/><path d="M5 2a2 2 0 0 1 2 2c0 1.5-2 4-2 4S3 5.5 3 4a2 2 0 0 1 2-2z" fill="#fff"/><circle cx="5" cy="4" r="0.8" fill="var(--navy)"/></svg>
      <span>Falkenried Metallbau GmbH<br>Am Werkhof 7<br>90210 Talheim Deutschland</span>
    </li>
    <li>
      <svg class="contact-icon" viewBox="0 0 10 10" aria-hidden="true"><rect width="10" height="10" rx="1.5" fill="var(--teal)"/><path d="M3 2.2l1.2 1.6-.6.8c.4.8 1 1.4 1.8 1.8l.8-.6 1.6 1.2-.7 1c-2.6-.4-4.7-2.5-5.1-5.1z" fill="#fff"/></svg>
      <span>+49 (0) 1234 56789-0</span>
    </li>
    <li>
      <svg class="contact-icon" viewBox="0 0 10 10" aria-hidden="true"><rect width="10" height="10" rx="1.5" fill="var(--teal)"/><rect x="2" y="3" width="6" height="4" fill="none" stroke="#fff" stroke-width="0.8"/><path d="M2 3l3 2.3L8 3" fill="none" stroke="#fff" stroke-width="0.8"/></svg>
      <span>m.keller@falkenried-gruppe.de</span>
    </li>
    <li>
      <svg class="contact-icon" viewBox="0 0 10 10" aria-hidden="true"><rect width="10" height="10" rx="1.5" fill="var(--teal)"/><path d="M3.5 2.2v5.2l1.3-1.2 1 2 .8-.4-1-2h1.8z" fill="#fff"/></svg>
      <span>www.falkenried-mb.de</span>
    </li>
  </ul>

  <svg class="band" viewBox="0 0 350 12" aria-hidden="true">
    <polygon points="0,2 167,2 175,11 0,11" fill="var(--teal)"/>
    <line x1="170" y1="6.5" x2="350" y2="6.5" stroke="var(--navy)" stroke-width="1"/>
  </svg>
</section>

</body>
</html>
```